Dynamic Book Cover Design
Lines That Hold
Creative Brief
ABOUT THE PROJECT "Lines That Hold: Seven Notes from a Counselor" is a practical, warm, and deeply insightful self-help ebook written by a licensed therapist (Morgan Pellow, LPC). Unlike generic self-help books that treat boundaries like a list of aggressive demands you make on other people, this book flips the script. The core concept is that a true boundary is an internal decision about yourself. One that holds firm no matter how the other person reacts. It is about self-possession, peace, and clarity. The book will be featured on my private practice website and on Quillmart. The cover needs to instantly communicate trust, professional clinical authority, and approachable warmth. I want it to look like a book you would see prominently displayed in a high-end wellness boutique or a psychology section, rather than a loud, busy, or flashy paperback. THE DESIGN DIRECTION Style: Clean, modern, uncluttered, and grounded. Tone: Firm but kind. Calm rather than aggressive. Typography: The title needs to be highly legible and crisp, even at thumbnail size on Quillmart. Thank you so much for your time and creativity. I can't wait to see how you bring this concept to life!
Health
Adults who feel drained, over-committed, or taken advantage of, and who struggle to say no or hold a limit. Broad appeal, leaning slightly female but not exclusively. These are thoughtful readers, not looking for hype. The cover should feel calm, credible, and reassuring, like something a good therapist would hand you. But still interesting to look at.
CREATIVE FREEDOM & METAPHORS I am entirely open to your creative interpretation! If you want to use a visual metaphor for a "boundary", please do. However, I want to completely steer clear of cliché, heavy-handed imagery. Please AVOID: • Brick walls, fences, barbed wire, or stop signs. • "No" symbols or literal hands pushing someone away. • Harsh reds or alarm-style, anxiety-inducing imagery. • Cheesy, dated stock photos. • Anything that feels cold, sterile, or overly clinical. BRANDING & COLORS This book is an extension of my therapy practice, so the cover design must feel cohesive with my existing brand. Please visit my website at https://morganpellowcounsel.example to view my current color palette, aesthetic, and font family (Montserrat). I want the book to feel like it naturally belongs in that digital space. DELIVERABLES REQUIRED • Front Ebook Cover (optimized for digital/Quillmart) • Full wrap layout including a spine and back cover (for potential future print runs)

```html
<!DOCTYPE html>
<html lang="en">
<head>
<meta charset="utf-8">
<title>Lines That Hold — Full Wrap Cover</title>
<link rel="stylesheet" href="https://fonts.googleapis.com/css2?family=Cormorant+Garamond:ital,wght@0,500;0,600;0,700;1,500&family=Montserrat:wght@400;500;600;700&display=swap">
<style>
  :root {
    --paper: #f4efe6;
    --paper-deep: #ece4d6;
    --forest: #2f4a36;
    --forest-deep: #263d2c;
    --sage: #5d7a5f;
    --clay: #a26a3f;
    --wheat: #d8b985;
    --ink: #3a3a34;
    --cream: #f3ead9;
  }
  * { margin: 0; padding: 0; box-sizing: border-box; }
  html, body { width: 1200px; height: 799px; overflow: hidden; background: var(--paper); }
  body { font-family: "Montserrat", sans-serif; color: var(--ink); }

  .wrap { position: relative; width: 1200px; height: 799px; display: flex; }

  /* Back cover */
  .back-cover {
    width: 486px; height: 799px; position: relative;
    background: linear-gradient(180deg, var(--paper) 0%, var(--paper-deep) 100%);
    padding: 22px 40px 0 44px;
  }
  .back-headline {
    font-family: "Cormorant Garamond", serif; font-weight: 600;
    font-size: 23px; line-height: 1.12; color: var(--forest);
  }
  .back-headline em { color: var(--clay); font-style: italic; }
  .back-intro { margin-top: 20px; font-size: 9.5px; line-height: 1.6; max-width: 370px; }
  .back-label {
    margin-top: 16px; font-size: 10px; font-weight: 700; letter-spacing: 0.06em;
    color: var(--forest); text-transform: uppercase;
  }
  .back-body { margin-top: 8px; font-size: 9.5px; line-height: 1.6; max-width: 370px; }
  .learn-label { margin-top: 18px; font-size: 9.5px; font-weight: 700; letter-spacing: 0.06em; color: var(--clay); text-transform: uppercase; }
  .learn-list { list-style: none; margin-top: 10px; }
  .learn-list li { display: flex; align-items: center; gap: 10px; font-size: 9.5px; line-height: 1; margin-bottom: 9px; }
  .tick { width: 14px; height: 14px; flex: none; }
  .back-closing { margin-top: 14px; font-size: 9.5px; line-height: 1.6; max-width: 360px; }
  .practice-mark { position: absolute; left: 44px; bottom: 58px; display: flex; align-items: center; gap: 10px; }
  .practice-dot { width: 18px; height: 18px; border-radius: 50%; background: var(--sage); }
  .practice-name { font-size: 12px; font-weight: 600; letter-spacing: 0.12em; color: var(--forest); text-transform: uppercase; line-height: 1.3; }
  .practice-role { font-size: 7px; font-weight: 500; letter-spacing: 0.12em; color: var(--ink); }
  .practice-url { position: absolute; left: 44px; bottom: 30px; font-size: 8.5px; color: var(--ink); }

  /* Spine */
  .spine {
    width: 60px; height: 799px; background: var(--forest); overflow: hidden;
    display: flex; flex-direction: column; align-items: center; padding-top: 18px;
  }
  .spine-dot { width: 12px; height: 12px; border-radius: 50%; border: 1.5px solid var(--wheat); flex: none; }
  .spine-text {
    writing-mode: vertical-rl; margin-top: 28px; display: flex; align-items: center;
  }
  .spine-title { font-family: "Cormorant Garamond", serif; font-weight: 600; font-size: 32px; line-height: 1; color: var(--cream); white-space: nowrap; }
  .spine-title span { color: var(--wheat); }
  .spine-sub { margin-top: 24px; font-size: 8px; letter-spacing: 0.14em; color: var(--cream); text-transform: uppercase; white-space: nowrap; }
  .spine-author-block { margin-top: 40px; text-align: start; }
  .spine-author { display: block; font-size: 11px; font-weight: 600; letter-spacing: 0.18em; line-height: 1.6; color: var(--cream); white-space: nowrap; }
  .spine-role { display: block; font-size: 6px; letter-spacing: 0.12em; line-height: 1.8; color: var(--wheat); white-space: nowrap; }

  /* Front cover */
  .front-cover { position: relative; width: 654px; height: 799px; overflow: hidden; }
  .front-scene {
    position: absolute; inset: 0;
    background:
      radial-gradient(ellipse 60% 22% at 50% 50%, rgba(255,236,200,0.9), rgba(255,236,200,0) 70%),
      linear-gradient(180deg, #f6f0e6 0%, #f3e8d6 32%, #ecd6b5 46%, #b9ae92 55%, #8e977f 63%, #a9a58c 70%, #cfc2ad 78%, #b9a58a 100%);
  }
  .front-content { position: relative; text-align: center; padding-top: 52px; }
  .front-title {
    font-family: "Cormorant Garamond", serif; font-weight: 600; color: var(--forest);
    font-size: 82px; line-height: 0.95; letter-spacing: -0.01em;
  }
  .front-title .accent { display: block; color: var(--clay); }
  .front-subtitle {
    margin: 22px auto 0; display: flex; align-items: center; justify-content: center; gap: 14px;
    font-size: 13px; font-weight: 600; letter-spacing: 0.12em; color: var(--forest); text-transform: uppercase;
  }
  .front-subtitle::before, .front-subtitle::after { content: ""; width: 34px; height: 1px; background: var(--forest); }
  .front-tagline {
    margin: 14px auto 0; max-width: 430px;
    font-family: "Cormorant Garamond", serif; font-style: italic; font-weight: 500;
    font-size: 18px; line-height: 1.3; color: var(--ink);
  }
  .front-author { position: absolute; left: 0; right: 0; bottom: 62px; text-align: center; }
  .front-author-name { font-size: 27px; font-weight: 500; letter-spacing: 0.16em; color: var(--forest-deep); }
  .front-author-role { margin-top: 6px; font-size: 11px; font-weight: 500; letter-spacing: 0.16em; color: var(--forest-deep); }
</style>
</head>
<body>
<main class="wrap">

  <section class="back-cover">
    <h2 class="back-headline">Better boundaries.<br>Stronger relationships.<br>A life that feels like <em>your</em> own.</h2>
    <p class="back-intro">If you've ever felt resentful, overwhelmed, or invisible in your relationships, you're not alone. Most people were never taught how to set boundaries that actually stick.</p>
    <p class="back-label">This book will show you a different way:</p>
    <p class="back-body">In seven simple notes, counselor Morgan Pellow offers a practical framework for setting limits that are clear, kind, and consistent—without guilt or overexplaining.</p>
    <p class="learn-label">You'll learn how to:</p>
    <ul class="learn-list">
      <li><svg class="tick" viewBox="0 0 14 14"><circle cx="7" cy="7" r="7" fill="#5d7a5f"/><path d="M4 7.2l2 2 4-4.2" stroke="#f4efe6" stroke-width="1.5" fill="none"/></svg>Build boundaries that hold, no matter how others respond</li>
      <li><svg class="tick" viewBox="0 0 14 14"><circle cx="7" cy="7" r="7" fill="#5d7a5f"/><path d="M4 7.2l2 2 4-4.2" stroke="#f4efe6" stroke-width="1.5" fill="none"/></svg>Stop over-giving and start taking care of yourself</li>
      <li><svg class="tick" viewBox="0 0 14 14"><circle cx="7" cy="7" r="7" fill="#5d7a5f"/><path d="M4 7.2l2 2 4-4.2" stroke="#f4efe6" stroke-width="1.5" fill="none"/></svg>Communicate your needs with confidence and calm</li>
      <li><svg class="tick" viewBox="0 0 14 14"><circle cx="7" cy="7" r="7" fill="#5d7a5f"/><path d="M4 7.2l2 2 4-4.2" stroke="#f4efe6" stroke-width="1.5" fill="none"/></svg>Handle pushback without second-guessing yourself</li>
      <li><svg class="tick" viewBox="0 0 14 14"><circle cx="7" cy="7" r="7" fill="#5d7a5f"/><path d="M4 7.2l2 2 4-4.2" stroke="#f4efe6" stroke-width="1.5" fill="none"/></svg>Create relationships based on respect, not obligation</li>
      <li><svg class="tick" viewBox="0 0 14 14"><circle cx="7" cy="7" r="7" fill="#5d7a5f"/><path d="M4 7.2l2 2 4-4.2" stroke="#f4efe6" stroke-width="1.5" fill="none"/></svg>Feel more at peace in your daily life</li>
    </ul>
    <p class="back-closing">Boundaries aren't about keeping people out.<br>They're about creating a life that <em>you</em> can thrive in.</p>
    <div class="practice-mark">
      <span class="practice-dot"></span>
      <div>
        <div class="practice-name">Morgan Pellow</div>
        <div class="practice-role">LICENSED PROFESSIONAL COUNSELOR</div>
      </div>
    </div>
    <p class="practice-url">morganpellowcounsel.example</p>
  </section>

  <aside class="spine">
    <span class="spine-dot"></span>
    <div class="spine-text">
      <span class="spine-title">Lines <span>That Hold</span></span>
      <span class="spine-sub">Seven notes from a counselor</span>
      <div class="spine-author-block">
        <span class="spine-author">MORGAN PELLOW</span>
        <span class="spine-role">LICENSED PROFESSIONAL COUNSELOR</span>
      </div>
    </div>
  </aside>

  <section class="front-cover">
    <div class="front-scene" role="img" aria-label="Calm photograph of a misty river valley at sunrise, with a mug, a closed notebook and a potted olive sprig on a stone table in the foreground"></div>
    <div class="front-content">
      <h1 class="front-title">Lines<span class="accent">That Hold</span></h1>
      <p class="front-subtitle">Seven notes from a counselor</p>
      <p class="front-tagline">A practical, compassionate guide to setting limits that protect your time, energy, and well-being—without guilt.</p>
    </div>
    <div class="front-author">
      <p class="front-author-name">MORGAN PELLOW</p>
      <p class="front-author-role">LICENSED PROFESSIONAL COUNSELOR</p>
    </div>
  </section>

</main>
</body>
</html>
```